Wordpress Theme Design for Family Law Firm

Hello, this is a WordPress theme design project, for a "Divorce and Family Law Mediation" practice.

I'd want the wordpress theme to be modeled loosely on this existing design from another one of our own sites: http://www.harbor-ledger-replies.example/

We want it to be bright and vibrant and convey a happy and relaxed feeling. The lines on it to not be sharp so more of the rounded edges and subtle shadows that you see on the example site.

Although built on WordPress, the site will be mostly static with fixed content pages, but including a blog feature.

The images will need to be different, but conveying a similar look and feel as the sample site. The colors from the sample site are close to what I'd like - but open to creative options.

It's important that the site looks professional, as well as friendly, and conveys the idea of mediation and relationships.

Important note: Traditional divorce website is for people looking to fight or being bullied.

Divorce mediation is for couples who have decided to split amicably so they're in a much more cooperative state of mind. There's not as much stress and anger. It's just about HOW we go about finalizing the process. There's light at the end of the tunnel.

With that in mind, the site should look friendly and happy, with an inspiring theme of a bright future.

Target Market(s)

The target market are people looking for amicable resolution, with a happy and uplifting attitude..

Traditional divorce websites are for people generally looking to fight or being bullied.

Divorce mediation (this website) is for couples who have decided to split amicably so they're in a much more cooperative state of mind. There's not as much stress and anger. It's just about HOW we go about finalizing the process. There's light at the end of the tunnel.

Industry/Entity Type

Family Law

Requirements
Must have
• Must have option for 1 or two sidebars for pages. This is because some of the internal pages will only have a single sidebar.

The footer will have the option for widgets.

```html
<!DOCTYPE html>
<html lang="en">
<head>
<meta charset="utf-8">
<title>Meridian Law Group</title>
<link href="https://fonts.googleapis.com/css2?family=Jost:ital,wght@0,400;0,500;1,400;1,500;1,600&family=PT+Sans:ital,wght@0,400;0,700;1,400;1,700&display=swap" rel="stylesheet">
<style>
:root{
  --navy:#2f3f7a;
  --navy-dark:#243163;
  --navy-light:#3d4f8f;
  --page:#f3f3f3;
  --text:#5a5a5a;
  --heading:#2d3b76;
  --panel:#e3e3e3;
  --panel-border:#c9c9c9;
  --white:#ffffff;
  --band:#e2e2e2;
}
*{box-sizing:border-box;margin:0;padding:0}
html,body{width:1200px;height:1162px;overflow:hidden}
body{background:var(--page);font-family:"PT Sans",sans-serif;color:var(--text);position:relative}
.abs{position:absolute}
.top-band{left:0;top:0;width:1200px;height:7px;background:var(--navy)}
.brand{left:243px;top:40px;display:flex;align-items:center;gap:10px}
.brand-mark{width:34px;height:34px;border-radius:50%;background:#4a8cc9}
.brand-name{font-family:"Jost",sans-serif;font-weight:400;font-size:26px;color:var(--navy);letter-spacing:2px;line-height:1}
.call{right:240px;top:60px;display:flex;align-items:center;gap:6px}
.call-text{font-size:9px;line-height:11px;text-align:right;color:var(--heading)}
.call-number{font-family:"Jost",sans-serif;font-size:21px;color:var(--heading)}
.main-nav{left:240px;top:131px;width:720px;height:38px;display:flex;border-radius:6px;overflow:hidden;
  background:linear-gradient(#4658a0,var(--navy-dark));box-shadow:0 2px 4px rgba(0,0,0,.3)}
.main-nav a{width:90px;display:flex;align-items:center;justify-content:center;color:#fff;text-decoration:none;
  font-family:"Jost",sans-serif;font-size:11px;border-right:1px solid rgba(0,0,0,.2)}
.main-nav a.wide{width:180px}
.main-nav a:last-child{border-right:none}
.hero{left:240px;top:206px;width:720px;height:225px;border-radius:8px;overflow:hidden;box-shadow:0 2px 6px rgba(0,0,0,.4)}
.hero-photo{position:absolute;inset:0;background:linear-gradient(100deg,#3a4573 0%,#4c567e 38%,#8c8ea0 55%,#b9b8bd 70%,#6a6b72 85%,#1c1d22 100%)}
.hero-title{position:absolute;left:44px;top:74px;font-family:"Jost",sans-serif;font-style:italic;font-weight:600;font-size:28px;line-height:36px;color:#fff;text-shadow:0 1px 3px rgba(0,0,0,.5)}
.hero-dots{position:absolute;left:101px;top:200px;display:flex;gap:7px}
.hero-dots span{width:8px;height:8px;border-radius:50%;background:#9a9aa3}
.hero-dots span.active{background:#fff}
.feature{top:469px;width:225px;height:141px;border-radius:6px;border:2px solid #5567a8;
  background:linear-gradient(#3b4c8c,var(--navy-dark));box-shadow:0 1px 3px rgba(0,0,0,.3);padding:14px 14px 0}
.feature h3{display:flex;align-items:center;gap:7px;font-style:italic;font-weight:400;font-size:13.5px;color:#fff;height:22px}
.feature p{margin-top:8px;font-size:8.8px;line-height:13.6px;color:#f0f0f0}
.btn{display:inline-block;margin-top:11px;padding:6px 8px;border-radius:4px;background:linear-gradient(#f4f4f4,#c9c9c9);
  font-style:italic;font-weight:700;font-size:9.5px;color:var(--navy);box-shadow:0 1px 2px rgba(0,0,0,.4)}
.welcome-title{left:240px;top:644px;font-family:"Jost",sans-serif;font-weight:500;font-size:20px;color:var(--heading)}
.welcome-photo{left:240px;top:686px;width:187px;height:112px;background:linear-gradient(90deg,#d9d9d9,#eeeeee 40%,#b3b3b3 70%,#3a3a3a);border:1px solid #ccc}
.welcome-copy{left:240px;top:683px;width:452px;font-size:8.8px;line-height:13.6px;color:var(--text)}
.welcome-copy .float{float:left;width:203px;height:120px}
.welcome-copy p+p{margin-top:13.6px}
.news{left:735px;top:649px;width:225px;height:225px;border-radius:6px;border:1px solid var(--panel-border);background:var(--panel);padding:11px 15px}
.news h2{font-family:"Jost",sans-serif;font-weight:500;font-size:19px;color:var(--heading);margin-bottom:8px}
.news-item{padding-left:7px;font-size:8.8px;line-height:13.6px;margin-bottom:13.6px}
.news-item em{display:block;color:#333;font-style:italic}
.section-title{top:908px;font-family:"Jost",sans-serif;font-style:italic;font-weight:400;font-size:14.5px;color:var(--heading)}
.contact-form{left:240px;top:942px;width:450px;height:93px;border-radius:6px;background:var(--navy)}
.field{position:absolute;height:21px;background:#fff;font-style:italic;font-size:8.5px;color:#555;padding:5px 14px;overflow:hidden}
.submit{position:absolute;left:368px;top:52px;width:67px;height:24px;border-radius:4px;background:linear-gradient(#f4f4f4,#c6c6c6);
  font-style:italic;font-weight:700;font-size:10px;color:var(--navy);display:flex;align-items:center;justify-content:center;box-shadow:0 1px 2px rgba(0,0,0,.4)}
.testimonial{left:735px;top:942px;width:225px;height:93px;border-radius:6px;border:1px solid var(--panel-border);background:#f0f0f0;
  padding:12px 14px;font-style:italic;font-size:8px;line-height:13.6px;color:#444}
.testimonial b{font-style:normal;color:#222}
.footer-nav{left:0;top:1072px;width:1200px;height:38px;background:var(--band);display:flex;justify-content:center;align-items:center;gap:15px;font-size:8.8px;color:#555}
.footer-bar{left:0;top:1110px;width:1200px;height:52px;background:var(--navy);color:#fff;font-size:8.8px}
.copyright{left:239px;top:19px}
.follow{right:240px;top:12px;display:flex;align-items:center;gap:6px}
.follow i{width:17px;height:17px;border-radius:3px;background:#dde3f2;display:block}
</style>
</head>
<body>
<div class="abs top-band"></div>

<div class="abs brand"><span class="brand-mark"></span><span class="brand-name">MERIDIAN LAW GROUP</span></div>

<div class="abs call">
  <div class="call-text">Call today for a<br>Free Phone Consultation</div>
  <svg width="18" height="32" viewBox="0 0 18 32"><path d="M6 2c-4 2-5 10-4 16 1 6 4 12 8 12l4-2c1-1 1-2 0-3l-3-4c-1-1-2-1-3 0l-1 1c-2-3-2-9-1-12l1 0c1 0 2-1 2-2l-1-5c0-1-1-2-2-1z" fill="#222"/></svg>
  <div class="call-number">555.014.2270</div>
</div>

<nav class="abs main-nav">
  <a>Home</a><a>Firm Overview</a><a>Attorney Profile</a><a class="wide">Divorce &amp; Family Law Mediation</a><a>Testimonials</a><a>Blog</a><a>Contact</a>
</nav>

<section class="abs hero">
  <div class="hero-photo" role="img" aria-label="Photo: family silhouette walking hand in hand at sunset"></div>
  <h1 class="hero-title">You can get a<br>right solutions</h1>
  <div class="hero-dots"><span class="active"></span><span></span><span></span><span></span></div>
</section>

<article class="abs feature" style="left:240px">
  <h3><svg width="24" height="22" viewBox="0 0 24 22"><path d="M2 12l6 7L22 2" fill="none" stroke="#7cc13a" stroke-width="4" stroke-linecap="round"/></svg>You can get a right solution</h3>
  <p>Lorem Ipsum is simply dummy text of the print-ing and typesetting industry. Lorem Ipsum is simply dummy text of the printing.</p>
  <span class="btn">Learn More</span>
</article>
<article class="abs feature" style="left:488px">
  <h3><svg width="26" height="22" viewBox="0 0 26 22"><rect x="3" y="3" width="12" height="6" rx="1" transform="rotate(-35 9 6)" fill="#d98a3a"/><path d="M10 9l12 10" stroke="#c9c9c9" stroke-width="3" stroke-linecap="round"/><rect x="1" y="17" width="12" height="3" rx="1" fill="#d98a3a"/></svg>Our Services</h3>
  <p>Lorem Ipsum is simply dummy text of the print-ing and typesetting industry. Lorem Ipsum is simply dummy text of the printing.</p>
  <span class="btn">Learn More</span>
</article>
<article class="abs feature" style="left:735px">
  <h3><svg width="24" height="22" viewBox="0 0 24 24"><circle cx="12" cy="12" r="9" fill="none" stroke="#fff" stroke-width="5"/><circle cx="12" cy="12" r="9" fill="none" stroke="#e0472b" stroke-width="5" stroke-dasharray="7 7.1"/></svg>How can we help</h3>
  <p>Lorem Ipsum is simply dummy text of the print-ing and typesetting industry. Lorem Ipsum is simply dummy text of the printing.</p>
  <span class="btn">Learn More</span>
</article>

<h2 class="abs welcome-title">Welcome to our Site</h2>
<div class="abs welcome-photo" role="img" aria-label="Photo: attorney in a consultation with a client"></div>
<div class="abs welcome-copy">
  <div class="float"></div>
  <p>"Lorem ipsum dolor sit amet, consectetur adipisicing elit, sed do eiusmod tempor incididunt ut labore et dolore magna aliqua. Ut enim ad minim veniam, quis nostrud exercitation ullamco laboris nisi ut aliquip ex ea commodo consequat. Duis aute irure dolor in reprehenderit in voluptate velit esse cillum dolore eu fugiat nulla pariatur. Excepteur sint occae-cat cupidatat non proident, sunt in culpa qui officia dese-runt mollit anim id est laborum."</p>
  <p>"Lorem ipsum dolor sit amet, consectetur adipisicing elit, sed do eiusmod tempor incididunt ut labore et dolore magna aliqua. Ut enim ad minim veniam, quis nostrud exercitation ullamco laboris nisi ut aliquip ex ea commodo consequat. Duis aute irure dolor in reprehenderit in voluptate velit esse cillum dolore eu fugiat nulla pariatur. Excepteur sint occaecat cupidatat non proident, sunt in culpa qui officia deserunt mollit anim id est laborum."</p>
</div>

<aside class="abs news">
  <h2>Latest News</h2>
  <div class="news-item">It has survived not only five centuries, but also the leap into electronic typesetting,<em>Novermber 2012</em></div>
  <div class="news-item">It has survived not only five centuries, but also the leap into electronic unchanged.<em>September 2012</em></div>
  <div class="news-item">It has survived not only five centuries, remaining essentially unchanged.<em>August 2012</em></div>
</aside>

<h2 class="abs section-title" style="left:238px">Email us with your questions</h2>
<form class="abs contact-form">
  <div class="field" style="left:7px;top:14px;width:143px">Name</div>
  <div class="field" style="left:157px;top:14px;width:143px">Email</div>
  <div class="field" style="left:307px;top:14px;width:136px">Phone</div>
  <div class="field" style="left:7px;top:40px;width:353px;height:37px">Your Message</div>
  <div class="submit">Submit</div>
</form>

<h2 class="abs section-title" style="left:734px">“ What our Clients say</h2>
<blockquote class="abs testimonial">“It was popularised in the 1960s with the release of Typeline Lorem Ipsum passages, and desktop publishing software like Folio Layout including Folio Layout including Folio Layout including Lorem Ipsum. ” - <b>Daniel Avery, Oregon</b>.</blockquote>

<nav class="abs footer-nav">
  <span>Home</span><span>|</span><span>Firm Overview</span><span>|</span><span>Attorney Profile</span><span>|</span><span>Divorce &amp; Family Mediation</span><span>|</span><span>Testimonials</span><span>|</span><span>Blog</span><span>|</span><span>Contact us</span>
</nav>
<footer class="abs footer-bar">
  <div class="abs copyright">Copyright © 2012 Meridian Law Group. All rights reserved.</div>
  <div class="abs follow">Follow us on&nbsp;<i></i><i></i><i></i><i></i></div>
</footer>
</body>
</html>
```